Lumora Fabrix
A technical textile company
Lumora Fabrix -
Creative Brief
Professional
Ravi Kapoorji
Business Manager
117, Neel Kamal Residency Chandan Path , Moti Nagar Jaipur - 302049 Rajasthan , India
ravi.kapoorji@lumora-fabrix.example
www.lumora-fabrix.example
Skype : ravikelmora.. Also want - letter head - envelope - power point slide ( both first and regular pages) designs .
Address has to go in the back 117, Neel Kamal Residency Chandan Path , Moti Nagar Jaipur - 302049 Rajasthan , India

```html
<!DOCTYPE html>
<html lang="en">
<head>
<meta charset="utf-8">
<title>Lumora Fabrix – Business Cards</title>
<link rel="stylesheet" href="https://fonts.googleapis.com/css2?family=Arimo:ital,wght@0,400;0,700;1,700&display=swap">
<style>
  :root {
    --bg: #e6e4e1;
    --white: #ffffff;
    --ink: #333333;
    --muted: #555555;
    --orange: #c4520f;
    --orange-dark: #9c3a08;
    --orange-light: #e0721f;
    --navy: #0f3556;
    --navy-dark: #0a2440;
    --navy-light: #1d5f8c;
    --brand-blue: #1f5b96;
  }
  * { margin: 0; padding: 0; box-sizing: border-box; }
  html, body { width: 1200px; height: 953px; overflow: hidden; }
  body {
    background: var(--bg);
    font-family: "Arimo", Arial, sans-serif;
    position: relative;
  }
  .card {
    position: absolute;
    width: 451px;
    height: 250px;
    box-shadow: 0 4px 14px rgba(0,0,0,0.25);
  }
  .card--front { left: 373px; top: 40px; background: var(--white); }
  .card--back-white { left: 167px; top: 314px; background: var(--white); }
  .card--back-orange {
    left: 618px; top: 314px;
    background: radial-gradient(ellipse at 50% 35%, var(--orange-light), var(--orange) 55%, var(--orange-dark));
  }
  .card--back-navy {
    left: 386px; top: 580px;
    background: radial-gradient(ellipse at 50% 30%, var(--navy-light), var(--navy) 55%, var(--navy-dark));
  }

  .brand {
    display: flex; align-items: center; gap: 8px;
    font-weight: 700; font-size: 21px; color: var(--brand-blue);
    white-space: nowrap;
  }
  .brand__dot { width: 14px; height: 14px; border-radius: 50%; background: var(--orange); flex: none; }
  .brand--light { color: var(--white); }
  .brand--light .brand__dot { background: var(--white); }

  .card--front .brand { position: absolute; left: 30px; top: 112px; }
  .divider { position: absolute; top: 70px; width: 1px; height: 110px; background: #9a9a9a; }
  .card--front .divider { left: 210px; }

  .contact { position: absolute; left: 226px; top: 72px; font-size: 11px; line-height: 16px; color: var(--ink); }
  .contact__name { font-size: 18px; font-weight: 700; color: var(--orange); line-height: 20px; }
  .contact__title { font-size: 11px; color: var(--muted); margin-bottom: 14px; }
  .contact__label { font-weight: 700; color: var(--orange); }

  .card--back-white .brand { position: absolute; left: 30px; top: 114px; font-size: 19px; }
  .card--back-white .divider { left: 225px; top: 82px; height: 90px; }
  .address { font-size: 10.5px; line-height: 17px; color: var(--ink); }
  .card--back-white .address { position: absolute; left: 240px; top: 86px; }

  .centered {
    position: absolute; inset: 0;
    display: flex; flex-direction: column; align-items: center; justify-content: center;
    gap: 26px; padding-top: 10px;
  }
  .centered .brand { font-size: 22px; }
  .address--light { color: var(--white); text-align: center; line-height: 16px; }
</style>
</head>
<body>

  <section class="card card--front" aria-label="Business card front">
    <div class="brand"><span class="brand__dot"></span>Lumora Fabrix</div>
    <div class="divider"></div>
    <div class="contact">
      <div class="contact__name">Ravi Kapoorji</div>
      <div class="contact__title">Business Manager</div>
      <div><span class="contact__label">Skype :</span> ravikelmora</div>
      <div><span class="contact__label">Cell :</span> +91 90012 34567</div>
      <div><span class="contact__label">Email :</span> ravi.kapoorji@lumora-fabrix.example</div>
      <div><span class="contact__label">Web :</span> www.lumora-fabrix.example</div>
    </div>
  </section>

  <section class="card card--back-white" aria-label="Business card back, white">
    <div class="brand"><span class="brand__dot"></span>Lumora Fabrix</div>
    <div class="divider"></div>
    <div class="address">
      117, Neel Kamal Residency<br>
      Chandan Path , Moti Nagar<br>
      Jaipur - 302049<br>
      Rajasthan , India
    </div>
  </section>

  <section class="card card--back-orange" aria-label="Business card back, orange">
    <div class="centered">
      <div class="brand brand--light"><span class="brand__dot"></span>Lumora Fabrix</div>
      <div class="address address--light">
        117, Neel Kamal Residency, Chandan Path ,<br>
        Moti Nagar, Jaipur - 302049<br>
        Rajasthan , India
      </div>
    </div>
  </section>

  <section class="card card--back-navy" aria-label="Business card back, navy">
    <div class="centered">
      <div class="brand brand--light"><span class="brand__dot"></span>Lumora Fabrix</div>
      <div class="address address--light">
        117, Neel Kamal Residency, Chandan Path ,<br>
        Moti Nagar, Jaipur - 302049<br>
        Rajasthan , India
      </div>
    </div>
  </section>

</body>
</html>
```